Re-design a highly converting profile page for my website

My website allows people to book a mentor for long-term mentorship as well as sessions. I would like to re-design this site within our branding guidelines to give people the best profile possible.

Please give this website a modern look and concentrate on the CTA and conversion rates. This is a highly converting site and it should stay that way or even get better!

Please also keep menu bar & footer in tact

Target Market(s)

Developers, Designers, Entrepreneurs in the Tech industry

Number of Pages Required

1 page

Requirements
Must have
• Strong CTA, existing color palette, testimonials and major elements
Nice to have
• Modern look, easy to see CTA, easy to scan offer. Not too crowded
Should not have
• No reporpusing. It is and stays a profile page

```html
<!DOCTYPE html>
<html lang="en">
<head>
<meta charset="utf-8">
<title>Mentor Profile – GuideHarbor</title>
<link href="https://fonts.googleapis.com/css2?family=Montserrat:wght@400;500;600;700&family=Inter:wght@400;500;600&display=swap" rel="stylesheet">
<style>
:root{
  --page:#f7f7f7;
  --card:#ffffff;
  --navy:#2c3b52;
  --ink:#30343b;
  --muted:#6f7680;
  --soft:#a5abb3;
  --line:#e3e7ec;
  --teal:#1dd1ae;
  --teal-soft:#8fe2d1;
  --blue:#2f7fe0;
  --star:#f7962b;
  --footer:#e3e9f1;
}
*{margin:0;padding:0;box-sizing:border-box}
html,body{width:678px;height:1200px;overflow:hidden}
body{background:var(--page);font-family:"Montserrat",sans-serif;color:var(--ink);position:relative}
.abs{position:absolute}
.logo-dot{position:absolute;border-radius:50%;background:var(--navy)}
.nav-item{position:absolute;top:27px;font-size:6.4px;font-weight:600;letter-spacing:.16em;color:#1f2430}
.nav-item .chev{color:var(--teal);font-size:5px;margin-left:3px}
.btn{position:absolute;display:flex;align-items:center;justify-content:center;font-weight:600;letter-spacing:.12em;text-transform:uppercase}
.btn-login{left:518px;top:22px;width:42px;height:17px;background:var(--teal-soft);color:#3e8a7c;font-size:6.2px}
.btn-start{left:576px;top:22px;width:59px;height:17px;background:var(--navy);color:#fff;font-size:6.2px}
.card{position:absolute;background:var(--card);border-radius:4px}
.avatar{position:absolute;border-radius:50%;background:radial-gradient(circle at 45% 40%,#5a5a5a,#111 70%);box-shadow:0 0 0 2px #fff,0 0 0 3px #dfe3e8}
.avatar.warm{background:radial-gradient(circle at 45% 40%,#c8a38c,#6d4a3c 75%)}
.avatar.cool{background:radial-gradient(circle at 45% 40%,#b7b9a5,#5f6b6d 75%)}
.avatar.rose{background:radial-gradient(circle at 45% 40%,#d8b2a0,#4d2a26 75%)}
.name-row{position:absolute;display:flex;align-items:center;gap:8px;white-space:nowrap}
.name{font-size:13px;font-weight:600;letter-spacing:.12em;color:#1f2430}
.badge{background:var(--teal);color:#fff;border-radius:2px;font-size:5.6px;letter-spacing:.14em;display:flex;align-items:center;justify-content:center;text-transform:uppercase;white-space:nowrap}
.small{font-size:6px;color:var(--muted);letter-spacing:.12em}
.pill{position:absolute;background:#e9ecef;border-radius:4px;font-size:5.8px;color:var(--muted);letter-spacing:.14em;display:flex;align-items:center;justify-content:center}
.title{font-size:8.4px;font-weight:500;letter-spacing:.14em;color:#4a4f57;white-space:nowrap}
.social{position:absolute;width:7px;height:7px;border-radius:50%}
.social.fb{background:#2f6fd6}.social.tw{background:#2aa3ef}.social.li{background:#0b6fb0}.social.wa{background:#25c16a}
.save{position:absolute;border:1px solid var(--line);border-radius:2px;font-size:4.4px;color:var(--muted);display:flex;align-items:center;justify-content:center;letter-spacing:.1em}
.feature{position:absolute;font-size:5.2px;letter-spacing:.12em;color:#555b63;white-space:nowrap}
.ficon{position:absolute;width:7px;height:7px;border:1px solid var(--teal);border-radius:50%}
.bio{position:absolute;left:158px;width:274px;font-size:5.7px;line-height:7.15px;letter-spacing:.06em;color:#5b6068}
.section-h{position:absolute;font-size:6.8px;letter-spacing:.14em;color:#3b4049;white-space:nowrap}
.skill{position:absolute;left:173px;font-size:5.4px;letter-spacing:.1em;color:#4a4f57}
.track{position:absolute;left:216px;width:169px;height:1px;background:#dfe6ee}
.fill{position:absolute;left:0;top:-0.5px;height:2px;background:var(--teal)}
.knob{position:absolute;top:-2px;width:5px;height:5px;border-radius:50%;background:var(--teal-soft)}
.skill-val{position:absolute;left:390px;font-size:5.2px;color:var(--soft);letter-spacing:.08em}
.stars{color:var(--star);letter-spacing:.04em}
.star-row{position:absolute;left:166px;font-size:6.8px;letter-spacing:.06em;color:#b9c0c8}
.star-row.on{color:var(--blue)}
.star-bar{position:absolute;left:202px;width:63px;height:1px;background:#dfe6ee}
.star-bar.on{background:var(--star);height:1.2px}
.star-count{position:absolute;left:275px;font-size:6.8px;color:#b9c0c8;letter-spacing:.06em}
.star-count.on{color:var(--blue)}
.rev-name{position:absolute;left:189px;font-size:7.4px;letter-spacing:.12em;color:#2b8c7c;font-weight:500}
.rev-date{position:absolute;left:190px;font-size:7px;letter-spacing:.12em;color:var(--teal)}
.rev-text{position:absolute;left:190px;width:258px;font-size:5.5px;line-height:7.2px;letter-spacing:.04em;color:#6b7078;text-transform:uppercase}
.rev-pub{position:absolute;left:190px;font-size:4.6px;letter-spacing:.12em;color:#c7ccd2}
.side-h{position:absolute;left:496px;width:139px;text-align:center;font-size:6.8px;letter-spacing:.14em;color:#3b4049;white-space:nowrap}
.btn-apply{left:515px;top:150px;width:99px;height:18px;background:var(--teal);color:#fff;font-size:6px;border-radius:3px}
.btn-reserve{left:515px;top:180px;width:99px;height:18px;background:var(--navy);color:#fff;font-size:6px;border-radius:3px}
.note{position:absolute;left:496px;width:139px;text-align:center;font-size:4.9px;font-style:italic;letter-spacing:.08em;color:var(--muted);line-height:6px}
.rb-label{position:absolute;left:522px;font-size:6px;letter-spacing:.12em;color:#4a4f57}
.rb-val{position:absolute;left:594px;font-size:6px;letter-spacing:.06em;color:#4a4f57}
.expect{position:absolute;left:515px;width:120px;font-size:5px;line-height:6px;letter-spacing:.05em;color:#6b7078;text-transform:uppercase}
.dot{position:absolute;left:510px;width:2px;height:2px;border-radius:50%;background:var(--navy)}
.brief-h{position:absolute;left:515px;font-size:6.1px;letter-spacing:.12em;color:#3b4049}
.brief-h::before{content:"";position:absolute;left:-5px;top:2px;width:2px;height:2px;border-radius:50%;background:var(--blue)}
.brief-s{position:absolute;left:515px;font-size:4.6px;letter-spacing:.06em;color:var(--muted);white-space:nowrap}
.tag{position:absolute;width:36px;height:7px;border-radius:4px;background:#eef1f4;font-size:4.2px;color:#8a9098;letter-spacing:.1em;display:flex;align-items:center;justify-content:center}
.related-h{position:absolute;left:78px;top:844px;font-size:10.3px;font-weight:500;letter-spacing:.14em;color:#555b63}
.rc{position:absolute;top:884px;width:240px;height:135px;background:#fff;border-radius:4px}
.rc .avatar{left:6px;top:-1px;width:32px;height:32px}
.rc .name-row{left:46px;top:3px;gap:7px}
.rc-name{font-size:9px;font-weight:600;letter-spacing:.12em;color:#1f2430}
.rc-title{position:absolute;left:46px;top:18px;font-size:7px;font-weight:500;letter-spacing:.08em;color:#4a4f57;white-space:nowrap}
.rc-meta{position:absolute;top:34px;font-size:4.9px;letter-spacing:.12em;color:var(--muted);white-space:nowrap}
.rc-desc{position:absolute;left:49px;top:52px;width:160px;font-size:6.1px;line-height:7.2px;font-style:italic;letter-spacing:.07em;color:#5b6068}
.rc-match{position:absolute;left:49px;top:86px;width:180px;font-size:6.1px;line-height:7.2px;letter-spacing:.07em;color:#5b6068}
.rc-match b{color:var(--teal);font-weight:500}
.rc-last{position:absolute;left:46px;top:110px;font-size:5px;letter-spacing:.12em;color:var(--muted)}
.rc-price{position:absolute;right:20px;top:108px;font-size:7.6px;letter-spacing:.1em;color:#3b4049;text-align:right}
.rc-price span{color:var(--teal)}
.rc-spots{position:absolute;right:10px;top:120px;font-size:5px;letter-spacing:.12em;color:var(--muted)}
.arrow{position:absolute;top:938px;width:14px;height:14px}
.footer{position:absolute;left:0;top:1050px;width:678px;height:150px;background:var(--footer);font-family:"Inter",sans-serif}
.f-brand{position:absolute;left:67px;top:42px;font-size:7.2px;font-weight:600;color:var(--navy)}
.f-text{position:absolute;left:67px;font-size:7.3px;color:#3a4150;line-height:11px}
.f-link{position:absolute;font-size:6.9px;color:#2f3644;letter-spacing:.02em}
</style>
</head>
<body>

<header class="site-nav">
  <div class="logo-dot" style="left:43px;top:21px;width:19px;height:19px"></div>
  <div class="nav-item" style="left:251px">FIND A MENTOR<span class="chev">&#8964;</span></div>
  <div class="nav-item" style="left:341px">FOR BUSINESSES<span class="chev">&#8964;</span></div>
  <div class="nav-item" style="left:435px">BOOK A SESSION</div>
  <div class="btn btn-login">Login</div>
  <div class="btn btn-start">Get Started</div>
</header>

<main class="card profile" style="left:42px;top:78px;width:420px;height:735px"></main>

<div class="avatar" role="img" aria-label="Mentor portrait photo" style="left:80px;top:80px;width:42px;height:42px"></div>
<div class="social fb" style="left:78px;top:149px"></div>
<div class="social tw" style="left:97px;top:149px"></div>
<div class="social li" style="left:118px;top:149px"></div>
<div class="save" style="left:76px;top:165px;width:31px;height:9px"><span style="color:#f0386b;margin-right:3px">&#9829;</span>SAVE</div>
<div class="save" style="left:112px;top:165px;width:15px;height:9px">20</div>

<div class="name-row" style="left:158px;top:88px">
  <div class="name">RAFAEL MENDES</div>
  <div class="badge" style="width:44px;height:9px">Verified</div>
</div>
<div class="abs small" style="right:225px;top:90px;font-weight:500;color:#4a4f57">4 SPOTS AVAILABLE</div>
<svg class="abs" style="left:159px;top:107px" width="6" height="8" viewBox="0 0 6 8"><path d="M3 0a3 3 0 0 1 3 3c0 2-3 5-3 5S0 5 0 3a3 3 0 0 1 3-3z" fill="#1dd1ae"/><circle cx="3" cy="3" r="1.1" fill="#fff"/></svg>
<div class="abs small" style="left:172px;top:108px">UNITED KINGDOM</div>
<div class="abs small" style="left:164px;top:122px;color:#3b4049;font-weight:500">RATINGS 5.0 <i style="font-weight:400;color:var(--muted);letter-spacing:.08em;margin-left:3px">(4 reviews)</i></div>
<div class="pill" style="left:158px;top:135px;width:89px;height:8px">8 MENTORED CLIENTS</div>
<div class="abs title" style="left:158px;top:148px">SENIOR SOFTWARE ENGINEER - CODEWELL</div>

<div class="ficon" style="left:162px;top:174px"></div><div class="feature" style="left:177px;top:175px">1-ON-1 CALLS</div>
<div class="ficon" style="left:162px;top:183px"></div><div class="feature" style="left:177px;top:185px">PERSONAL CHAT</div>
<div class="ficon" style="left:261px;top:174px"></div><div class="feature" style="left:274px;top:175px">CHALLENGES &amp; PROJECTS</div>
<div class="ficon" style="left:261px;top:183px"></div><div class="feature" style="left:274px;top:185px">HANDS-ON SUPPORT</div>
<div class="ficon" style="left:371px;top:174px"></div><div class="feature" style="left:385px;top:175px">PERSONAL CHAT</div>

<p class="bio" style="top:211px">I am a versatile Senior Software Engineer and a Tech Evangelist. I hold a bachelor of technology's degree in Geology with 6+ years experience building incredible software products and balancing client urgency in conjunction with technological complexity of developing these products for globally distributed teams. designing and developing solutions to solve complex technical problems.</p>
<p class="bio" style="top:254px">I have successfully interacted with diverse programming languages and technologies. At the core is Python, Javascript and Ruby with emphasis on frameworks such as React, Vue.js, Nodejs, Expressjs, Ruby On Rails, Flask and Django. I have built Restful and GraphQL APIs alike. I have also worked with databases such as PostgreSQL, MySQL, MongoDB and Redis for Caching/Job Queues. I have experience using cloud API gateways, cloud websocket gateways, serverless functions and content delivery networks.</p>
<p class="bio" style="top:311px">I am enthusiastic about developing practical business solutions using my skill sets. I am constantly in pursuit of knowledge, passionate about a fast-paced, challenging opportunity and agile work environment, not just to push the boundaries of my knowledge and positively impact my growth but to improve the quality of the teams I work with and better the lives of people around me. I am really into developing E-commerce applications and love to learn more about Machine Learning and Artificial Intelligence to help improve the E-commerce space.</p>
<p class="bio" style="top:375px">I enjoy setting up opportunities for learning. Served as mentor/speaker in various Code Sisters, Open Learn Club, Teen Builders and other meetup group events. I also write technical and non-technical articles alike.</p>

<div class="section-h" style="left:159px;top:416px">SKILLS TAUGHT BY MENTOR</div>
<div class="skill" style="top:443px">PYTHON</div><div class="track" style="top:446px"><div class="fill" style="width:127px"></div><div class="knob" style="left:125px"></div></div><div class="skill-val" style="top:443px">7.9/10</div>
<div class="skill" style="top:452px">RUBY</div><div class="track" style="top:455px"><div class="fill" style="width:86px"></div><div class="knob" style="left:84px"></div></div><div class="skill-val" style="top:452px">6.4/10</div>
<div class="skill" style="top:461px">RAILS</div><div class="track" style="top:464px"><div class="fill" style="width:107px"></div><div class="knob" style="left:105px"></div></div><div class="skill-val" style="top:461px">7.9/10</div>
<div class="skill" style="top:471px">JAVASCRIPT</div><div class="track" style="top:474px"><div class="fill" style="width:168px"></div><div class="knob" style="left:166px"></div></div><div class="skill-val" style="top:471px">9.7/10</div>
<div class="skill" style="top:480px">REACT</div><div class="track" style="top:483px"><div class="fill" style="width:147px"></div><div class="knob" style="left:145px"></div></div><div class="skill-val" style="top:480px">7.9/10</div>

<div class="section-h" style="left:158px;top:506px">REVIEWS(4) <span class="stars" style="margin-left:6px;font-size:6px">★★★★★</span> <span style="color:#3b4049;font-weight:600">5</span></div>
<div class="star-row on" style="top:521px">5 Stars</div><div class="star-bar on" style="top:525px"></div><div class="star-count on" style="top:521px">(4)</div>
<div class="star-row" style="top:532px">4 Stars</div><div class="star-bar" style="top:536px"></div><div class="star-count" style="top:532px">(0)</div>
<div class="star-row" style="top:546px">3 Stars</div><div class="star-bar" style="top:550px"></div><div class="star-count" style="top:546px">(0)</div>
<div class="star-row" style="top:561px">2 Stars</div><div class="star-bar" style="top:565px"></div><div class="star-count" style="top:561px">(0)</div>
<div class="star-row" style="top:576px">1 Stars</div><div class="star-bar" style="top:580px"></div><div class="star-count" style="top:576px">(0)</div>

<article class="review">
  <div class="avatar cool" role="img" aria-label="Reviewer portrait photo" style="left:159px;top:613px;width:24px;height:24px;box-shadow:none"></div>
  <div class="rev-name" style="top:616px">LENA HARTWELL</div>
  <div class="rev-date" style="top:627px">2020 JAN 30</div>
  <p class="rev-text" style="top:641px">Rafael is clear and concise in his guidance, and he strives to be always prompt to respond to my requests. Overall, I totally recommend him as a great person, developer and mentor!</p>
  <div class="rev-pub" style="top:669px">PUBLISHED 2 WEEKS AGO</div>
</article>
<article class="review">
  <div class="avatar rose" role="img" aria-label="Reviewer portrait photo" style="left:159px;top:687px;width:24px;height:24px;box-shadow:none"></div>
  <div class="rev-name" style="top:690px">LENA HARTWELL</div>
  <div class="rev-date" style="top:700px">2020 JAN 30</div>
  <p class="rev-text" style="top:714px">Rafael is clear and concise in his guidance, and he strives to be always prompt to respond to my requests. Overall, I totally recommend him as a great person, developer and mentor!</p>
  <div class="rev-pub" style="top:743px">PUBLISHED 2 WEEKS AGO</div>
</article>
<div class="abs" style="left:191px;top:761px;font-size:5.2px;letter-spacing:.12em;color:#2b8c7c">[MORE REVIEWS &#8964; ]</div>

<aside class="card" style="left:496px;top:78px;width:139px;height:182px"></aside>
<div class="side-h" style="top:92px;color:var(--blue);font-size:6px;font-weight:600">&#9654; 7 DAY FREE TRIAL!</div>
<div class="side-h" style="top:104px;color:var(--teal);font-size:16px;font-weight:600;letter-spacing:.08em">$150</div>
<div class="side-h" style="top:123px;font-size:9px;font-weight:500">PER MONTH</div>
<div class="btn btn-apply">Apply for mentorship</div>
<div class="btn btn-reserve">Reserve a session</div>
<div class="note" style="top:203px">* reseve a session is a one time<br>payment for a single session</div>
<div class="side-h" style="top:227px;font-size:6px">AVERAGE RESPONSE TIME</div>
<div class="side-h" style="top:238px;font-size:5.2px;color:var(--muted);letter-spacing:.1em"><span style="color:var(--teal)">&#9889;</span> responds within a few hours</div>

<aside class="card" style="left:496px;top:282px;width:139px;height:143px"></aside>
<div class="side-h" style="top:304px">RATING BREAKDOWN</div>
<div class="rb-label" style="top:326px">COMMUNICATION</div><div class="rb-val" style="top:326px">(5)<span class="stars">★</span></div>
<div class="rb-label" style="top:337px">FLEXIBLE</div><div class="rb-val" style="top:337px">(4)<span class="stars">★</span></div>
<div class="rb-label" style="top:349px">KNOWLEDGABLE</div><div class="rb-val" style="top:349px">(5)<span class="stars">★</span></div>
<div class="rb-label" style="top:360px">GOOD LISTNER</div><div class="rb-val" style="top:360px">(4)<span class="stars">★</span></div>
<div class="rb-label" style="top:372px">LOVE &amp; CANDID</div><div class="rb-val" style="top:372px">(4)<span class="stars">★</span></div>
<div class="abs" style="left:516px;top:387px;width:115px;font-size:4.6px;line-height:5.6px;letter-spacing:.1em;color:var(--muted)">* THESE REVIWES WERE TAKEN FROM THE CLIENT REVIEWS &amp; THORUGH OUR QUALITY ASSURING PROCEDURE</div>

<aside class="card" style="left:496px;top:446px;width:139px;height:143px"></aside>
<div class="dot" style="top:472px"></div>
<div class="abs" style="left:526px;top:467px;font-size:6.8px;letter-spacing:.14em;color:#3b4049">WHAT CAN I EXPECT?</div>
<div class="expect" style="top:482px">Unlimited access to the mentor via chat, e-mail or text, within reason</div><div class="dot" style="top:496px"></div>
<div class="expect" style="top:506px">You will have a 7 day trial for free with this mentor</div><div class="dot" style="top:515px"></div>
<div class="expect" style="top:525px">Will give you tasks and exercises to complete, if wanted</div><div class="dot" style="top:534px"></div>
<div class="expect" style="top:544px">Includes regular 1-on-1 calls, per agreement with mentor</div>
<div class="abs" style="left:515px;top:563px;font-size:5.3px;letter-spacing:.08em;color:var(--teal)">[ See More ]</div>

<aside class="card" style="left:496px;top:607px;width:139px;height:143px"></aside>
<div class="side-h" style="top:621px">BRIEF ABOUT MENTOR</div>
<div class="brief-h" style="top:643px">PROFFESION</div>
<div class="brief-s" style="top:653px">SENIOR SOFTWARE ENGINEER - CODEWELL</div>
<div class="brief-h" style="top:664px">EXPERIENCE AS MENTOR</div>
<div class="brief-s" style="top:674px">3 YEARS EXPERINCE <span style="color:var(--teal);font-weight:600">VERIFIED</span> MENTOR</div>
<div class="brief-h" style="top:686px">RATING</div>
<div class="brief-s" style="top:695px"><span style="color:var(--teal);font-weight:600">5.0</span> AVERAGE CLIENT &nbsp;REVIEW</div>
<div class="brief-h" style="top:707px">SKILLS</div>
<div class="tag" style="left:512px;top:715px">PHYTHON</div><div class="tag" style="left:553px;top:715px">HTML</div><div class="tag" style="left:593px;top:715px">RUBY</div>
<div class="tag" style="left:512px;top:727px">PHYTHON</div><div class="tag" style="left:553px;top:727px">HTML</div><div class="tag" style="left:593px;top:727px">RUBY</div>

<aside class="card" style="left:496px;top:767px;width:139px;height:46px"></aside>
<div class="side-h" style="top:779px">SUPPORT OTHERS BY SHARING</div>
<div class="social fb" style="left:526px;top:794px"></div>
<div class="social tw" style="left:549px;top:794px"></div>
<div class="social li" style="left:573px;top:794px"></div>
<div class="social wa" style="left:596px;top:794px"></div>

<h2 class="related-h">RELATED MONETORS</h2>
<svg class="arrow" style="left:53px" viewBox="0 0 14 14"><path d="M9 2 4 7l5 5" fill="none" stroke="#3b4049" stroke-width="1.6"/></svg>
<svg class="arrow" style="left:611px" viewBox="0 0 14 14"><path d="M5 2l5 5-5 5" fill="none" stroke="#3b4049" stroke-width="1.6"/></svg>

<section class="rc" style="left:77px">
  <div class="avatar" role="img" aria-label="Mentor portrait photo"></div>
  <div class="name-row"><div class="rc-name">RAFAEL MENDES</div><div class="badge" style="width:47px;height:7px;font-size:4.6px;letter-spacing:.06em">&#9679; NEW MENTOR</div></div>
  <div class="rc-title">SENIOR SOFTWARE ENGINEER - CODEWELL</div>
  <svg class="abs" style="left:46px;top:33px" width="5" height="7" viewBox="0 0 6 8"><path d="M3 0a3 3 0 0 1 3 3c0 2-3 5-3 5S0 5 0 3a3 3 0 0 1 3-3z" fill="#1dd1ae"/></svg>
  <div class="rc-meta" style="left:57px">UNITED KINGDOM</div>
  <div class="rc-meta" style="left:129px;color:#3b4049">RATINGS 5.0 <i style="color:var(--muted);margin-left:3px">(4 reviews)</i></div>
  <p class="rc-desc">Rafael Mendes is a Senior Software Engineer and a Tech Evangelist. He hold a bachelor of technology's degree in Geology with 6+ years experience in different inovative fields.</p>
  <p class="rc-match"><b>We believe</b> Rafael Mendes could be a good match for you too.</p>
  <div class="rc-last">LAST REVIEW <span class="stars" style="font-size:6px;margin-left:2px">★★★★★</span><br><span style="position:relative;top:2px;left:-1px">20TH MAY 20</span></div>
  <div class="rc-price"><span>$160</span> / Month</div>
  <div class="rc-spots">ONLY 4 SPOTS AVAILABLE</div>
</section>

<section class="rc" style="left:361px">
  <div class="avatar warm" role="img" aria-label="Mentor portrait photo"></div>
  <div class="name-row"><div class="rc-name">RAFAEL MENDES</div><div class="badge" style="width:47px;height:7px;font-size:4.6px;letter-spacing:.06em">&#9679; NEW MENTOR</div></div>
  <div class="rc-title">SENIOR SOFTWARE ENGINEER - CODEWELL</div>
  <svg class="abs" style="left:46px;top:33px" width="5" height="7" viewBox="0 0 6 8"><path d="M3 0a3 3 0 0 1 3 3c0 2-3 5-3 5S0 5 0 3a3 3 0 0 1 3-3z" fill="#1dd1ae"/></svg>
  <div class="rc-meta" style="left:57px">UNITED KINGDOM</div>
  <div class="rc-meta" style="left:129px;color:#3b4049">RATINGS 5.0 <i style="color:var(--muted);margin-left:3px">(4 reviews)</i></div>
  <p class="rc-desc">Rafael Mendes is a Senior Software Engineer and a Tech Evangelist. He hold a bachelor of technology's degree in Geology with 6+ years experience in different inovative fields.</p>
  <p class="rc-match"><b>We believe</b> Rafael Mendes could be a good match for you too.</p>
  <div class="rc-last">LAST REVIEW <span class="stars" style="font-size:6px;margin-left:2px">★★★★★</span><br><span style="position:relative;top:2px;left:-1px">20TH MAY 20</span></div>
  <div class="rc-price"><span>$160</span> / Month</div>
  <div class="rc-spots">ONLY 4 SPOTS AVAILABLE</div>
</section>

<footer class="footer">
  <div class="logo-dot" style="left:67px;top:26px;width:12px;height:12px"></div>
  <div class="f-brand">GuideHarbor</div>
  <p class="f-text" style="top:55px">Your trusted source to find highly-vetted mentors<br>&amp; industry professionals to move your career ahead.</p>
  <p class="f-text" style="top:81px">© 2020 GuideHarbor. All Rights Reserved.</p>
  <div class="social" style="left:67px;top:96px;background:#2f3644"></div>
  <div class="social" style="left:89px;top:96px;background:#2f3644"></div>
  <div class="f-link" style="left:344px;top:56px">BROWSE MENTORS</div>
  <div class="f-link" style="left:344px;top:70px">BECOME A MENTOR</div>
  <div class="f-link" style="left:344px;top:83px">PARTNER PROGRAM</div>
  <div class="f-link" style="left:344px;top:97px">FAQ</div>
  <div class="f-link" style="left:344px;top:111px">BLOG</div>
  <div class="f-link" style="left:484px;top:56px">ABOUT US</div>
  <div class="f-link" style="left:484px;top:70px">CODE OF CONDUCT</div>
  <div class="f-link" style="left:484px;top:83px">PRIVACY POLICY</div>
  <div class="f-link" style="left:484px;top:97px">SUCCESS STORIES</div>
  <div class="f-link" style="left:484px;top:111px;font-weight:600;color:var(--navy)">INFO@GUIDEHARBOR.COM</div>
</footer>

</body>
</html>
```